Therapy Department Recruitment Flyer

Recruitment flyer similar to nursing one attached but for Occupational Therapy and Physical Therapy. Please use pictures depicting therapy services being provided to elderly population.

```html
<!DOCTYPE html>
<html lang="en">
<head>
<meta charset="utf-8">
<title>Therapist Positions – Silver Ridge Care Center</title>
<link rel="stylesheet" href="https://fonts.googleapis.com/css2?family=Dancing+Script:wght@400&family=Ubuntu+Condensed:wght@400&family=Ubuntu:wght@300;400;500&display=swap">
<style>
  :root {
    --navy: #0e3e8a;
    --green: #5a9f5c;
    --ink: #2e3a4e;
    --grey-band: #e1e1e1;
    --grey-tri: #d0d0d0;
    --backdrop: #333333;
    --white: #ffffff;
  }
  * { margin: 0; padding: 0; box-sizing: border-box; }
  html, body { width: 1200px; height: 1200px; overflow: hidden; background: var(--backdrop); }
  .flyer {
    position: absolute; left: 262px; top: 65px;
    width: 695px; height: 985px;
    transform: scale(1.0909); transform-origin: 0 0;
    background: var(--white);
    overflow: hidden;
    font-family: "Ubuntu", sans-serif;
  }
  .flyer-shapes { position: absolute; inset: 0; }
  .brand-mark {
    position: absolute; left: 536px; top: 339px; width: 124px; height: 124px;
    border-radius: 50%; background: var(--ink);
    display: flex; align-items: center; justify-content: center; text-align: center;
    color: var(--white); font-family: "Ubuntu Condensed", "Arial Narrow", sans-serif; font-size: 14px; line-height: 1.3;
  }
  .headline {
    position: absolute; right: 16px; top: 474px;
    font-size: 46px; font-weight: 400; color: var(--ink); white-space: nowrap;
  }
  .subhead {
    position: absolute; right: 18px; top: 533px;
    font-size: 26px; font-weight: 300; color: var(--ink); white-space: nowrap;
  }
  .about {
    position: absolute; left: 0; top: 594px; width: 345px; text-align: center; color: var(--white);
  }
  .about-title { font-size: 24px; font-weight: 400; margin-bottom: 17px; }
  .about-body {
    font-family: "Ubuntu Condensed", "Arial Narrow", sans-serif;
    font-size: 14px; line-height: 19.6px; padding: 0 16px;
  }
  .tagline {
    position: absolute; left: 383px; top: 600px; width: 280px; text-align: center;
    font-family: "Dancing Script", cursive; font-size: 24px; line-height: 28px; color: var(--ink);
  }
  .role {
    position: absolute; left: 394px; width: 259px; height: 61px; border-radius: 31px;
    color: var(--white); font-size: 17px; line-height: 24px;
  }
  .role-name { position: absolute; left: 0; width: 218px; top: 7px; text-align: center; }
  .role-check {
    position: absolute; right: 4px; top: 4px; width: 53px; height: 53px; border-radius: 50%;
    background: var(--white); display: flex; align-items: center; justify-content: center;
  }
  .role--pt { top: 725px; background: var(--navy); }
  .role--ot { top: 798px; background: var(--green); }
  .contact-label {
    position: absolute; left: 380px; width: 240px; top: 885px; text-align: center;
    font-family: "Ubuntu Condensed", "Arial Narrow", sans-serif; font-size: 18px; color: #333;
  }
  .footer {
    position: absolute; left: 0; right: 0; top: 918px; height: 67px; background: var(--grey-band);
    font-family: "Ubuntu Condensed", "Arial Narrow", sans-serif; font-size: 14px; color: #444; white-space: nowrap;
  }
  .footer-item { position: absolute; top: 0; height: 67px; display: flex; align-items: center; }
  .footer-item svg { margin-right: 6px; flex: none; }
  .footer-name { left: 27px; }
  .footer-phone { left: 257px; }
  .footer-email { left: 425px; }
  .name-first { color: var(--navy); }
  .name-last { color: var(--green); }
</style>
</head>
<body>
<main class="flyer">
  <svg class="flyer-shapes" viewBox="0 0 695 985" width="695" height="985">
    <defs>
      <linearGradient id="photoTone" x1="0" y1="0" x2="1" y2="1">
        <stop offset="0" stop-color="#c9b8a6"/>
        <stop offset="0.45" stop-color="#9fb3c8"/>
        <stop offset="1" stop-color="#dfe6ee"/>
      </linearGradient>
      <linearGradient id="panelTone" x1="0" y1="0" x2="0" y2="1">
        <stop offset="0.35" stop-color="#5a9f5c"/>
        <stop offset="1" stop-color="#1f5ea8"/>
      </linearGradient>
    </defs>
    <polygon role="img" aria-label="Photo: therapist helping a smiling senior man stretch a blue resistance band overhead"
             points="0,0 695,0 695,250 175,510 0,405" fill="url(#photoTone)"/>
    <polygon points="600,295 695,250 695,340" fill="var(--grey-tri)"/>
    <polygon points="0,405 175,510 0,595" fill="var(--navy)"/>
    <polygon points="0,595 175,510 345,590 345,912 0,912" fill="url(#panelTone)"/>
  </svg>

  <div class="brand-mark">Silver Ridge<br>Care Center</div>

  <h1 class="headline">Therapist Positions</h1>
  <p class="subhead">Silver Ridge Care Center</p>

  <section class="about">
    <h2 class="about-title">Silver Ridge Care Center</h2>
    <p class="about-body">is a Skilled Nursing Facility in Alder Creek, Nevada.<br>At the heart of Juniper County, Alder Creek is a friendly, rural mountain town in Eastern Nevada that is rich with art &amp; history, as well in abundance of opportunities for outdoor adventure.</p>
  </section>

  <p class="tagline">We are seeking<br>caring &amp; compassionate<br>therapist to join our team</p>

  <div class="role role--pt">
    <span class="role-name">PHYSICAL<br>THERAPIST</span>
    <span class="role-check"><svg width="34" height="30" viewBox="0 0 34 30"><path d="M3 16 L13 26 L31 3" fill="none" stroke="var(--green)" stroke-width="5" stroke-linecap="round" stroke-linejoin="round"/></svg></span>
  </div>
  <div class="role role--ot">
    <span class="role-name">OCCUPATIONAL<br>THERAPIST</span>
    <span class="role-check"><svg width="34" height="30" viewBox="0 0 34 30"><path d="M3 16 L13 26 L31 3" fill="none" stroke="var(--navy)" stroke-width="5" stroke-linecap="round" stroke-linejoin="round"/></svg></span>
  </div>

  <p class="contact-label">Recruiting Contact:</p>

  <footer class="footer">
    <span class="footer-item footer-name"><span class="name-first">DANA</span>&nbsp;<span class="name-last">MERCER</span>, Director of Rehab</span>
    <span class="footer-item footer-phone">
      <svg width="20" height="20" viewBox="0 0 20 20"><circle cx="10" cy="10" r="8.5" fill="none" stroke="var(--navy)" stroke-width="1.5"/><path d="M7 5.5 L8.6 7.8 L7.8 9 Q9 11.4 11 12.2 L12.2 11.4 L14.5 13 L13.4 14.6 Q9.5 14.6 6.5 10.5 Q5.4 7.5 7 5.5 Z" fill="var(--navy)"/></svg>
      555-014-2270 ext 1020
    </span>
    <span class="footer-item footer-email">
      <svg width="20" height="20" viewBox="0 0 20 20"><circle cx="10" cy="10" r="8.5" fill="none" stroke="var(--green)" stroke-width="1.5"/><rect x="5.5" y="7" width="9" height="6.5" fill="none" stroke="var(--green)" stroke-width="1.2"/><path d="M5.5 7 L10 10.8 L14.5 7" fill="none" stroke="var(--green)" stroke-width="1.2"/></svg>
      dmercer@silverridgecare.com
    </span>
  </footer>
</main>
</body>
</html>
```